brimSTONE corporation pty ltd

Contruction industry
It's a wall and floor tiling business

Industry/Entity Type

Business

Requirements
Must have
• Likes-
- clean and easy to read
- a witty design is always well received
- for it to look reputable in the industry
- a strong and direct presentation
- simple but striking colour selection
Should not have
• Dislikes-
- pls no tacky square tiles to resemble tiling

```html
<!DOCTYPE html>
<html lang="en">
<head>
<meta charset="utf-8">
<title>brimSTONE business card</title>
<link href="https://fonts.googleapis.com/css2?family=Open+Sans:wght@400;600;700;800&display=swap" rel="stylesheet">
<style>
  :root {
    --backdrop: #4a4a4a;
    --card-dark: #2a2a2b;
    --card-mid: #3a3a3b;
    --accent: #ea7b2b;
    --logo-grey: #c9c9c9;
    --text-light: #d6d6d6;
    --text-soft: #bdbdbd;
  }
  * { margin: 0; padding: 0; box-sizing: border-box; }
  html, body {
    width: 1200px; height: 534px; overflow: hidden;
    background: var(--backdrop);
    font-family: "Open Sans", Arial, sans-serif;
  }
  .stage { position: relative; width: 1200px; height: 534px; }
  .card {
    position: absolute; top: 119px; width: 517px; height: 295px; overflow: hidden;
    box-shadow: 0 4px 14px rgba(0,0,0,.45);
  }
  .card--front { left: 62px; }
  .card--back { left: 622px; }
  .card__surface {
    position: absolute; inset: 0;
    background: radial-gradient(ellipse at 45% 40%, var(--card-mid) 0%, var(--card-dark) 75%);
  }
  .card__band {
    position: absolute; left: 0; right: 0; top: 242px; height: 28px;
    background: var(--accent);
  }
  .brand { position: absolute; text-align: right; }
  .brand__name {
    display: block; font-weight: 800; color: var(--logo-grey);
    letter-spacing: -1px; line-height: 1;
  }
  .brand__tagline {
    display: block; font-weight: 700; color: var(--logo-grey); line-height: 1;
  }
  .card--front .brand { left: 68px; top: 108px; width: 380px; }
  .card--front .brand__name { font-size: 66px; }
  .card--front .brand__tagline { font-size: 16px; margin-top: 2px; }
  .card--back .brand { left: 50px; top: 124px; width: 200px; }
  .card--back .brand__name { font-size: 35px; }
  .card--back .brand__tagline { font-size: 9px; margin-top: 1px; }
  .contact { position: absolute; left: 309px; top: 88px; width: 208px; }
  .contact__name {
    font-size: 11.5px; font-weight: 700; color: var(--text-light); letter-spacing: .3px;
    padding: 0 0 4px 0; border-bottom: 2px solid var(--accent);
  }
  .contact__address { font-size: 10px; color: var(--text-soft); margin-top: 8px; }
  .contact__list { list-style: none; margin-top: 8px; }
  .contact__item {
    display: flex; align-items: center; gap: 12px;
    font-size: 10px; color: var(--text-soft); height: 16px;
  }
  .contact__icon { width: 13px; height: 12px; fill: var(--accent); flex: none; }
</style>
</head>
<body>
<main class="stage">
  <section class="card card--front">
    <div class="card__surface" role="img" aria-label="Dark charcoal card surface with a faint honeycomb texture"></div>
    <div class="brand">
      <span class="brand__name">brimSTONE</span>
      <span class="brand__tagline">corporation pty ltd</span>
    </div>
    <div class="card__band"></div>
  </section>

  <section class="card card--back">
    <div class="card__surface" role="img" aria-label="Dark charcoal card surface with a faint honeycomb texture"></div>
    <div class="brand">
      <span class="brand__name">brimSTONE</span>
      <span class="brand__tagline">corporation pty ltd</span>
    </div>
    <div class="contact">
      <p class="contact__name">MARA QUILL : CEO MANAGER</p>
      <p class="contact__address">123 Brimstone Street Ave, 4th Floor</p>
      <ul class="contact__list">
        <li class="contact__item">
          <svg class="contact__icon" viewBox="0 0 12 12"><path d="M3 1l2 2.5-1.2 1.2a7 7 0 0 0 3.5 3.5L8.5 7 11 9l-1.5 2C5 11 1 7 1 2.5z"/></svg>
          +000-000-0000
        </li>
        <li class="contact__item">
          <svg class="contact__icon" viewBox="0 0 12 12"><rect x="3" y="0.5" width="6" height="3"/><rect x="0.5" y="4" width="11" height="5" rx="1"/><rect x="3" y="8" width="6" height="3.5"/></svg>
          +000-000-0000
        </li>
        <li class="contact__item">
          <svg class="contact__icon" viewBox="0 0 12 12"><circle cx="6" cy="6" r="5.5"/></svg>
          www.yourwebsite.com
        </li>
        <li class="contact__item">
          <svg class="contact__icon" viewBox="0 0 12 12"><path d="M0.5 2h11v8h-11z M1 2.5l5 4 5-4" stroke="#2a2a2b" stroke-width="0.8"/></svg>
          yourname@email.com
        </li>
      </ul>
    </div>
    <div class="card__band"></div>
  </section>
</main>
</body>
</html>
```